Asia based real estate financing firm needs and AWESOME design for a biz card -Harborline Lending Partners

Looking for a stylish, & corporate-looking business card for a real estate financing brokerage firm in Asia, offering global mortgage loans. I uploaded our current logos. We would like to add a splash of color (perhaps the house icon) or any other suggestions are open. For the winning designer, we have a lot of work! Thanks and best of luck!

Target Market(s)

Real estate investors globally. We want to look more like a BANK and NOT a real estate company. Please don't play up on a "house" design.

Industry/Entity Type

Banking

Contact Information for Business Card

Harborline Lending Partners
Peter Walsh
Co-Founder | Partner

42 Kelvin Street, Suite 310
Singapore 074219
www.hlp-lend.example
peterwalsh@hlp-lend.example
+65 555-0147
WeChat: peterwalsh

Colors

Designer to choose colors to be used in the design.

Requirements
Must have
• Must have the standard business requirements for a card; name, address, email, etc
• Can be horizontal or vertical.
Nice to have
• It would be great to see some sort of variation to the logo with a pop of color. Red is good as we're in Asia, however, other options work as well.
• Our tag line is - Borderless mortgages. It doesn't have to be on the card but might be nice.
• I'd like to start seeing our tagline within the cards as well. - Borderless mortgages.
• Also, please add our location. The location for this card is Singapore so perhaps it can be highlighted or emphasised in some way.
• Singapore | Hong Kong | Shanghai | Manila
• As we will soon open an office in Shanghai, having an option for both languages would be great.
Should not have
• I'm exceited and open to your creativity ... knock it out of the park!

```html
<!DOCTYPE html>
<html lang="en">
<head>
<meta charset="utf-8">
<title>Harborline Lending Partners – Business Card</title>
<link rel="stylesheet" href="https://fonts.googleapis.com/css2?family=Open+Sans:wght@400;600&display=swap">
<style>
  :root {
    --backdrop: #2b2b2d;
    --card: #1b1b1d;
    --card-edge: #252527;
    --brand-blue: #3a6fc4;
    --brand-red: #d2272b;
    --silver: #8d8d91;
  }
  * { margin: 0; padding: 0; box-sizing: border-box; }
  html, body {
    width: 1200px; height: 900px; overflow: hidden;
    background: var(--backdrop);
    font-family: "Open Sans", Arial, sans-serif;
  }
  .stage { position: relative; width: 1200px; height: 900px; }
  .card {
    position: absolute; left: 320px; width: 560px; height: 330px;
    background: var(--card);
    border: 1px solid var(--card-edge);
    box-shadow: 0 8px 24px rgba(0,0,0,.35);
  }
  .card--front { top: 60px; display: flex; align-items: center; justify-content: center; }
  .card--back { top: 480px; }

  .wordmark { font-weight: 600; text-align: center; letter-spacing: 1px; }
  .wordmark--front { color: var(--silver); font-size: 34px; line-height: 1.25; }
  .wordmark--back {
    position: absolute; left: 28px; top: 118px; width: 210px;
    color: var(--brand-blue); font-size: 22px; line-height: 1.3; text-align: center;
  }

  .divider {
    position: absolute; left: 262px; top: 50px; width: 2px; height: 230px;
    background: var(--brand-blue);
  }

  .contact {
    position: absolute; left: 288px; top: 44px; width: 260px;
    color: var(--brand-blue); font-size: 16px; line-height: 1.3;
  }
  .contact__name { color: var(--brand-red); font-weight: 600; font-size: 20px; letter-spacing: .5px; }
  .contact__role { margin-bottom: 10px; }
  .contact__address { margin-bottom: 10px; }
  .contact__line { display: flex; align-items: center; gap: 8px; }
  .contact__line svg { width: 14px; height: 14px; flex: none; }
  .contact__wechat { color: var(--brand-red); }
</style>
</head>
<body>
<main class="stage">
  <section class="card card--front" aria-label="Card front">
    <p class="wordmark wordmark--front">Harborline<br>Lending Partners</p>
  </section>

  <section class="card card--back" aria-label="Card back">
    <p class="wordmark wordmark--back">Harborline<br>Lending Partners</p>
    <div class="divider"></div>
    <div class="contact">
      <p class="contact__name">PETER WALSH</p>
      <p class="contact__role">Co-Founder | Partner</p>
      <p class="contact__address">42 Kelvin Street<br>Suite 310<br>Singapore 074219</p>
      <p class="contact__line">
        <svg viewBox="0 0 14 14" aria-hidden="true"><circle cx="7" cy="7" r="6" fill="none" stroke="#d2272b" stroke-width="1.6"/><path d="M1 7h12M7 1c-3 3-3 9 0 12M7 1c3 3 3 9 0 12" fill="none" stroke="#d2272b" stroke-width="1.2"/></svg>
        www.hlp-lend.example
      </p>
      <p class="contact__line">
        <svg viewBox="0 0 14 14" aria-hidden="true"><rect x="1" y="3" width="12" height="8" fill="#d2272b"/><path d="M1 3l6 5 6-5" fill="none" stroke="#1b1b1d" stroke-width="1.2"/></svg>
        peterwalsh@hlp-lend.example
      </p>
      <p class="contact__line">
        <svg viewBox="0 0 14 14" aria-hidden="true"><path d="M3 1l2.5 3-1.5 1.5c.8 1.8 2.2 3.2 4 4L9.5 8l3 2.5-1.5 2.5C6 13 1 8 1 2.5z" fill="#d2272b"/></svg>
        +65 555-0147
      </p>
      <p class="contact__wechat">WeChat: peterwalsh</p>
    </div>
  </section>
</main>
</body>
</html>
```